Redesign business card for Wade Linford Construction

Basically I want a complete redesign of the business card I have attached with this project. The only stipulations I have are that the colors , crimson and white, stay the same and all of the information on the old card is also on the new design. Also I would like to add that we also specialize in metal building foundations as well. I look forward to seeing what you all come up with.
Industry/Entity Type
Business
Contact Information for Business Card
All of the details are on the attachment I have included with this project
Look and feel
Each slider illustrates characteristics of the customer's brand and the style your logo design should communicate.

```html
<!DOCTYPE html>
<html lang="en">
<head>
<meta charset="utf-8">
<title>Wade Linford Construction – Business Card</title>
<link href="https://fonts.googleapis.com/css2?family=Montserrat:wght@500;700&display=swap" rel="stylesheet">
<style>
  :root {
    --crimson: #e8212b;
    --white: #ffffff;
    --ink: #1c1c1c;
    --backdrop: #e9e9eb;
  }
  * { box-sizing: border-box; margin: 0; padding: 0; }
  html, body { width: 1200px; height: 800px; overflow: hidden; }
  body {
    background: var(--backdrop);
    font-family: "Montserrat", sans-serif;
    display: flex;
    align-items: center;
    justify-content: center;
    gap: 40px;
  }
  .card {
    width: 540px;
    height: 310px;
    border-radius: 14px;
    position: relative;
    overflow: hidden;
    box-shadow: 0 8px 24px rgba(0,0,0,0.15);
  }
  /* Front */
  .card-front {
    background: var(--crimson);
    color: var(--white);
    display: flex;
    flex-direction: column;
    align-items: center;
    justify-content: center;
    text-align: center;
  }
  .brand-dot {
    width: 96px; height: 96px;
    border: 6px solid var(--white);
    border-radius: 50%;
    margin-bottom: 22px;
  }
  .brand-name { font-weight: 700; font-size: 27px; letter-spacing: 0.2px; white-space: nowrap; }
  .brand-tag { font-weight: 700; font-size: 19px; margin-top: 4px; white-space: nowrap; }

  /* Back */
  .card-back { background: var(--white); color: var(--ink); }
  .contact { position: absolute; left: 30px; top: 24px; }
  .person-name { color: var(--crimson); font-weight: 700; font-size: 17px; letter-spacing: 0.4px; }
  .person-role { font-weight: 700; font-size: 10px; margin-bottom: 12px; }
  .address { font-size: 13.5px; line-height: 1.35; font-weight: 500; margin-bottom: 12px; }
  .contact-list { list-style: none; font-size: 13px; font-weight: 500; line-height: 1.5; }
  .contact-list li { display: flex; align-items: center; gap: 8px; white-space: nowrap; }
  .contact-list svg { width: 11px; height: 11px; fill: var(--crimson); flex-shrink: 0; }

  .back-brand {
    position: absolute; right: 22px; top: 22px; width: 200px;
    display: flex; flex-direction: column; align-items: center; text-align: center;
    color: var(--crimson);
  }
  .back-brand .brand-dot { width: 66px; height: 66px; border-color: var(--crimson); border-width: 5px; margin-bottom: 10px; }
  .back-brand .brand-name { font-size: 12.5px; }
  .back-brand .brand-tag { font-size: 10.5px; margin-top: 1px; }
  .founder { font-weight: 700; font-size: 11px; line-height: 1.3; margin-top: 8px; }

  .specialty-band {
    position: absolute; left: 0; right: 0; bottom: 20px; height: 50px;
    background: var(--crimson); color: var(--white);
    font-size: 12px; font-weight: 500; line-height: 1.35;
    display: flex; align-items: center; padding: 0 22px;
  }
</style>
</head>
<body>
  <section class="card card-front">
    <div class="brand-dot"></div>
    <div class="brand-name">Wade Linford Construction</div>
    <div class="brand-tag">Concrete Contractor</div>
  </section>

  <section class="card card-back">
    <div class="contact">
      <div class="person-name">JONAH LINFORD</div>
      <div class="person-role">Owner</div>
      <div class="address">218 East Mill Rd.<br>Riverton, AL 36110</div>
      <ul class="contact-list">
        <li><svg viewBox="0 0 24 24"><path d="M6.6 10.8a15.1 15.1 0 0 0 6.6 6.6l2.2-2.2a1 1 0 0 1 1-.25 11.4 11.4 0 0 0 3.6.57 1 1 0 0 1 1 1V20a1 1 0 0 1-1 1A17 17 0 0 1 3 4a1 1 0 0 1 1-1h3.5a1 1 0 0 1 1 1c0 1.250.2 2.450.57 3.57a1 1 0 0 1-.25 1z"/></svg>334.555.0147</li>
        <li><svg viewBox="0 0 24 24"><path d="M7 1h10a2 2 0 0 1 2 2v18a2 2 0 0 1-2 2H7a2 2 0 0 1-2-2V3a2 2 0 0 1 2-2zm0 3v14h10V4z"/></svg>334.555.0148</li>
        <li><svg viewBox="0 0 24 24"><path d="M12 3 2 12h3v9h5v-6h4v6h5v-9h3z"/></svg>334.555.0193</li>
        <li><svg viewBox="0 0 24 24"><path d="M2 5h20v14H2zm2 2v.5l8 5 8-5V7l-8 5z"/></svg>wlconstruction1992@mailbox.com</li>
      </ul>
    </div>

    <div class="back-brand">
      <div class="brand-dot"></div>
      <div class="brand-name">Wade Linford Construction</div>
      <div class="brand-tag">Concrete Contractor</div>
      <div class="founder">Founder<br>Wade Linford<br>“BEDROCK”</div>
    </div>

    <div class="specialty-band">Specializing in concrete foundations, metal building foundations, driveways, storm rooms, additions and most other form of concrete work</div>
  </section>
</body>
</html>
```